GLS biz card

We need a business card design for our new company based in Los Angeles called "Gold Lantern Studios". We develop film and television projects. We work with investors, financiers, film production companies, film distribution and sales companies as well as studios. We would like to incorporate our logo (see attached) on a two-sided card. We need to include: name and title, address, phone, email and company website.

Target Market(s)

Business, financial and studio clients

Industry/Entity Type

Business

Contact Information for Business Card

Two-sided. We are thinking of the logo on one side and the information on the back. Please feel free to be creative! Thanks.

Requirements
Must have
• Please include the following text information, excluding the "CAPS CATEGORY:" and please allow the ability for us to change the name, title and email address for each company employee):
• NAME & TITLE:
• Peter Dunmore
• Managing Partner
• COMPANY NAME:
• GOLD LANTERN STUDIOS (please use existing logo)
• COMPANY ADDRESS:
• KVT Arts Park
• 2480 Wexley Boulevard
• Arts Hall, 4th Floor
• Harbor Point, CA 90417
• COMPANY PHONE NUMBER:
• 310-555-4206
• COMPANY WEBSITE ADDRESS:
• www.goldlanternstudioshouse.com
• EMAIL ADDRESS: (only one per card)
• frank@goldlanternstudioshouse.com
• tizzy@goldlanternstudioshouse.com
• peter@goldlanternstudioshouse.com

```html
<!DOCTYPE html>
<html lang="en">
<head>
<meta charset="utf-8">
<title>Gold Lantern Studios – Business Card</title>
<link rel="stylesheet" href="https://fonts.googleapis.com/css2?family=Alegreya+Sans+SC:wght@300;400;500&display=swap">
<style>
  :root {
    --backdrop: #ececec;
    --card-dark: #050708;
    --card-light: #ffffff;
    --accent: #1aa9de;
    --ink: #151515;
  }
  * { margin: 0; padding: 0; box-sizing: border-box; }
  html, body { width: 1068px; height: 1200px; overflow: hidden; }
  body {
    background: var(--backdrop);
    font-family: "Alegreya Sans SC", "Trebuchet MS", sans-serif;
    color: var(--ink);
    position: relative;
  }
  .card {
    position: absolute;
    left: 203px;
    width: 679px;
    height: 397px;
    overflow: hidden;
  }
  .card--front { top: 166px; background: var(--card-dark); }
  .card--back { top: 655px; background: var(--card-light); }

  .brand { position: absolute; text-align: center; }
  .brand__dot {
    display: block;
    margin: 0 auto;
    border-radius: 50%;
    background: var(--accent);
  }
  .brand__name {
    display: block;
    font-weight: 500;
    color: var(--accent);
    letter-spacing: 0.08em;
    white-space: nowrap;
  }
  .card--front .brand { left: 0; right: 0; top: 83px; }
  .card--front .brand__dot { width: 142px; height: 142px; }
  .card--front .brand__name { font-size: 28px; margin-top: 24px; }

  .back__panel {
    position: absolute; left: 0; top: 0; bottom: 0;
    width: 272px;
    background: var(--card-dark);
    border-right: 5px solid var(--accent);
  }
  .back__panel .brand { left: 0; right: 0; top: 117px; }
  .back__panel .brand__dot { width: 94px; height: 94px; }
  .back__panel .brand__name { font-size: 18px; margin-top: 16px; }

  .back__info {
    position: absolute; left: 277px; right: 0; top: 0; bottom: 0;
  }
  .person { position: absolute; left: 0; right: 0; top: 36px; text-align: center; }
  .person__name { font-size: 35px; font-weight: 400; letter-spacing: 0.06em; line-height: 1; }
  .person__title { font-size: 21px; color: var(--accent); letter-spacing: 0.12em; margin-top: 6px; line-height: 1; }

  .rule {
    position: absolute; left: 19px; right: 27px;
    border-top: 1.5px dashed var(--accent);
  }
  .rule--top { top: 116px; }
  .rule--bottom { top: 234px; }

  .contacts { position: absolute; left: 22px; top: 131px; list-style: none; }
  .contacts li {
    display: flex; align-items: center;
    height: 31px;
    font-size: 16px; letter-spacing: 0.08em;
  }
  .contacts svg { width: 18px; height: 18px; margin-right: 10px; flex: none; }

  .address { position: absolute; left: 0; right: 0; top: 250px; text-align: center; font-style: normal; }
  .address svg { width: 14px; height: 18px; display: block; margin: 0 auto 4px; }
  .address__place { font-size: 21px; letter-spacing: 0.04em; line-height: 1.1; display: block; }
  .address__line { font-size: 15px; letter-spacing: 0.12em; line-height: 1.3; display: block; }
</style>
</head>
<body>
  <section class="card card--front" aria-label="Card front">
    <div class="brand">
      <span class="brand__dot"></span>
      <span class="brand__name">GOLD LANTERN STUDIOS</span>
    </div>
  </section>

  <section class="card card--back" aria-label="Card back">
    <div class="back__panel">
      <div class="brand">
        <span class="brand__dot"></span>
        <span class="brand__name">GOLD LANTERN STUDIOS</span>
      </div>
    </div>

    <div class="back__info">
      <div class="person">
        <h1 class="person__name">Peter Dunmore</h1>
        <p class="person__title">Film Director</p>
      </div>

      <div class="rule rule--top"></div>

      <ul class="contacts">
        <li>
          <svg viewBox="0 0 24 24" aria-hidden="true"><path fill="var(--accent)" d="M6.6 10.8a15 15 0 0 0 6.6 6.6l2.2-2.2c.3-.3.7-.4 1-.2 1.1.4 2.3.6 3.6.6.6 0 1 .4 1 1V20c0 .6-.4 1-1 1A17 17 0 0 1 3 4c0-.6.4-1 1-1h3.5c.6 0 1 .4 1 1 0 1.3.2 2.5.6 3.6.1.3 0 .7-.2 1z"/></svg>
          (310) 555 4206
        </li>
        <li>
          <svg viewBox="0 0 24 24" aria-hidden="true"><rect x="2.5" y="5.5" width="19" height="13" fill="none" stroke="var(--accent)" stroke-width="1.8"/><path d="M2.5 5.5 12 13l9.5-7.5" fill="none" stroke="var(--accent)" stroke-width="1.8"/></svg>
          peter@goldlanternstudioshouse.com
        </li>
        <li>
          <svg viewBox="0 0 24 24" aria-hidden="true"><circle cx="10" cy="10" r="6" fill="none" stroke="var(--accent)" stroke-width="2.4"/><path d="M14.5 14.5 21 21" stroke="var(--accent)" stroke-width="3" stroke-linecap="round"/></svg>
          goldlanternstudioshouse.com
        </li>
      </ul>

      <div class="rule rule--bottom"></div>

      <address class="address">
        <svg viewBox="0 0 14 18" aria-hidden="true"><path fill="var(--accent)" d="M7 0a7 7 0 0 0-7 7c0 5 7 11 7 11s7-6 7-11a7 7 0 0 0-7-7zm0 9.6A2.6 2.6 0 1 1 7 4.4a2.6 2.6 0 0 1 0 5.2z"/></svg>
        <span class="address__place">KVT Arts Park</span>
        <span class="address__line">2480 Wexley Boulevard</span>
        <span class="address__line">Arts Hall, 4th Floor</span>
        <span class="address__line">Harbor Point, CA 90417</span>
      </address>
    </div>
  </section>
</body>
</html>
```